BR7LUDO PSD Web Designs

We need website page designs for Ludo Capital, a start up HEDGE FUND MANAGEMENT business. 

Ludo means 'wave' in Greek, but this is not a Greek company.

You will need to create one template that will have some common elements (such as the menu) which you will then need to apply to 6 different pages.  

The site should:
• Incorporate the Ludo logo, colours and graphic elements provided with this brief.
• Have a corporate look with the provided corporate colours used in design. 
• Be professional and user-friendly 
• Have an international feel
• Be clean, clear and and easy to read
• Information to be organised in an easily accessible and logical way for time-pressed business people who are looking for efficient ways to check and manage their investment portfolios online.

We are looking for:
• Designs that do not just copy the wireframe
• Original thinking
• Extension of the brand that has already been created, throughout site.
• Design x-factor (structure, layout, readability, graphic elements)
• Corporate feel
• Judicious use of imagery (only use stock photos if they ADD meaning to your designs).

WIREFRAMES:
Attached are the wireframes of the pages that need to be designed.

Target Market(s)

Adults based in US, UK and Asia Pacific aged 25 to 70 who are corporate investors

Requirements
Must have
• Your submissions must:
• Include the logo we have attached and tie in with the business card look
• Use the menu as per the wireframes
• Include 6 PSDs (one for each of the attached wireframes)
1. Home
2. Contact Us
3. DIsclaimer
4. Our Focus
5. Privacy Policy
6. Risk Profile

```html
<!DOCTYPE html>
<html lang="en">
<head>
<meta charset="utf-8">
<title>Ludo Capital – Contact Us</title>
<link rel="stylesheet" href="https://fonts.googleapis.com/css2?family=Arimo:wght@400;700&display=swap">
<style>
:root{
  --navy:#0c2b5c;
  --blue:#1469ac;
  --deep:#0f5f9f;
  --sky:#3fb3e8;
  --pale:#a9dcf5;
  --label:#1b6db3;
  --heading:#4aa8dc;
  --field:#c5d3de;
  --line:#2d79b5;
  --white:#ffffff;
}
*{margin:0;padding:0;box-sizing:border-box}
html,body{width:1200px;height:900px;overflow:hidden;background:var(--white)}
body{font-family:"Arimo",Arial,sans-serif;color:var(--label)}
.canvas{position:relative;width:1280px;height:960px;transform:scale(.9375);transform-origin:0 0}
.abs{position:absolute}
.top-band{left:45px;top:0;width:1191px;height:44px;
  background:linear-gradient(180deg,var(--blue) 0%,var(--deep) 35%,var(--sky) 75%,var(--pale) 100%)}
.header-rule{left:45px;top:194px;width:1191px;height:1px;background:var(--line)}
.side-card{left:76px;top:40px;width:302px;height:565px;background:var(--white);
  box-shadow:0 0 14px rgba(0,0,0,.22)}
.brand{color:var(--navy);font-weight:700;letter-spacing:.5px;white-space:nowrap}
.brand-main{left:90px;top:92px;font-size:31px}
.brand .dot{display:inline-block;border-radius:50%;background:var(--navy);vertical-align:middle;margin-right:8px}
.brand-main .dot{width:16px;height:16px}
.brand-card{left:103px;top:314px;font-size:24px}
.brand-card .dot{width:12px;height:12px;margin-right:6px}
.side-heading{left:103px;top:236px;font-size:19px;font-weight:700;color:var(--heading)}
.company{left:103px;top:351px;font-size:18px;font-weight:700;color:var(--navy)}
.address{left:103px;top:372px;font-size:14.5px;line-height:17.6px;color:var(--label);font-style:normal}
.tab{top:158px;height:37px;width:188px;font-size:19px;color:var(--navy);text-align:center;line-height:44px}
.tab svg{position:absolute;left:0;top:0}
.tab span{position:relative}
.tab-focus{left:427px}
.tab-contact{left:624px}
.main-panel{left:400px;top:205px;width:598px;height:590px;background:var(--white);
  box-shadow:0 0 12px rgba(0,0,0,.18);overflow:hidden}
.right-panel{left:1011px;top:230px;width:201px;height:565px;background:var(--white);
  box-shadow:0 0 12px rgba(0,0,0,.18);overflow:hidden}
.panel-band{position:absolute;left:0;bottom:0;width:100%;height:30px;
  background:linear-gradient(180deg,var(--pale) 0%,var(--sky) 40%,var(--blue) 100%)}
.form-heading{font-size:19px;font-weight:700;color:var(--heading)}
.label{font-size:14.5px;color:var(--label);white-space:nowrap}
.field{height:16px;border:1px solid var(--field);background:var(--white);
  box-shadow:inset 1px 1px 2px rgba(0,0,0,.12)}
.check{width:16px;height:16px;border:1px solid var(--field);background:var(--white);
  box-shadow:inset 1px 1px 2px rgba(0,0,0,.12)}
.hint{font-size:8.5px;color:var(--label);white-space:nowrap}
.hint.slanted{font-style:italic}
.message{left:421px;top:602px;width:560px;height:129px;border:2px solid var(--field);
  box-shadow:inset 1px 1px 3px rgba(0,0,0,.1)}
.btn{height:22px;width:170px;text-align:center;font-size:15px;line-height:22px;color:var(--white);
  background:linear-gradient(180deg,#d9f1fc 0%,#8fd3f3 45%,#3fb0e6 100%);
  box-shadow:0 1px 2px rgba(0,0,0,.2)}
.btn-submit{left:421px;top:740px;width:148px;color:#eaf7fd;background:linear-gradient(180deg,#e4f5fd 0%,#a9def6 50%,#6cc5ee 100%)}
.quick-title{left:1011px;top:330px;width:201px;text-align:center;font-size:14.5px;color:var(--label)}
.quick-rule{left:1020px;top:350px;width:184px;height:1px;background:var(--line)}
.nav-btn{left:1027px;width:170px;font-size:15.5px}
.nav-btn.soft{color:var(--blue);font-size:14px;background:linear-gradient(180deg,#eaf7fd 0%,#a6dcf5 50%,#71c6ee 100%)}
.footer{left:45px;top:932px;width:1191px;height:21px;background:var(--blue);color:var(--white);
  font-size:11.5px;text-align:center;line-height:22px}
.footer .policy{color:var(--pale)}
</style>
</head>
<body>
<div class="canvas">

  <div class="abs top-band" role="img" aria-label="Decorative blue wave band across the page top"></div>
  <div class="abs header-rule"></div>

  <aside class="abs side-card"></aside>
  <div class="abs brand brand-main"><span class="dot"></span>LUDO CAPITAL</div>

  <div class="abs side-heading">By Phone</div>
  <div class="abs brand brand-card"><span class="dot"></span>LUDO CAPITAL</div>
  <div class="abs company">LUDO Capital Pty Ltd.</div>
  <address class="abs address">
    18/42 Bourke Row<br>Harbourside Vic 3999<br>Australia<br>Phone 03 9000 1234<br>Fax: 03 9000 5678<br>Email:ludo@ludocapital.example
  </address>

  <nav>
    <div class="abs tab tab-focus">
      <svg width="188" height="37" viewBox="0 0 188 37" aria-hidden="true">
        <defs><linearGradient id="tabBlue" x1="0" y1="0" x2="0" y2="1">
          <stop offset="0" stop-color="#c9ecfb"/><stop offset="1" stop-color="#45b4e7"/></linearGradient></defs>
        <path d="M0 37C10 30 14 2 30 1H168C182 1 180 30 188 37Z" fill="url(#tabBlue)" stroke="#2d79b5"/>
      </svg>
      <span>OUR FOCUS</span>
    </div>
    <div class="abs tab tab-contact">
      <svg width="188" height="37" viewBox="0 0 188 37" aria-hidden="true">
        <defs><linearGradient id="tabWhite" x1="0" y1="0" x2="0" y2="1">
          <stop offset="0" stop-color="#e6f6fd"/><stop offset=".5" stop-color="#ffffff"/><stop offset="1" stop-color="#ffffff"/></linearGradient></defs>
        <path d="M0 37C10 30 14 2 30 1H168C182 1 180 30 188 37Z" fill="url(#tabWhite)" stroke="#2d79b5"/>
      </svg>
      <span>CONTACT US</span>
    </div>
  </nav>

  <main class="abs main-panel">
    <div class="panel-band" role="img" aria-label="Decorative blue wave band along the panel foot"></div>
  </main>

  <div class="abs form-heading" style="left:425px;top:236px">Mail</div>
  <div class="abs label" style="left:424px;top:270px">First Name</div>
  <div class="abs field" style="left:505px;top:269px;width:186px"></div>
  <div class="abs label" style="left:715px;top:270px">Last Name</div>
  <div class="abs field" style="left:795px;top:269px;width:187px"></div>

  <div class="abs form-heading" style="left:425px;top:347px">Contact Phone</div>
  <div class="abs label" style="left:424px;top:381px">Country Code</div>
  <div class="abs field" style="left:518px;top:382px;width:61px"></div>
  <div class="abs label" style="left:604px;top:381px">Area Code</div>
  <div class="abs field" style="left:679px;top:382px;width:61px"></div>
  <div class="abs label" style="left:768px;top:381px">Ph. No</div>
  <div class="abs field" style="left:816px;top:382px;width:162px"></div>
  <div class="abs label" style="left:718px;top:414px">Email Address</div>
  <div class="abs field" style="left:816px;top:414px;width:162px"></div>
  <div class="abs hint" style="left:423px;top:443px">*Please enter the preferred number you would like us to contact you at</div>
  <div class="abs hint slanted" style="left:712px;top:443px">*Please enter the preferred email you would like us to contact you at</div>

  <div class="abs label" style="left:424px;top:484px">Prefferred Contact Method</div>
  <div class="abs label" style="left:638px;top:484px">Email</div>
  <div class="abs check" style="left:679px;top:483px"></div>
  <div class="abs label" style="left:770px;top:484px">Phone</div>
  <div class="abs check" style="left:817px;top:483px"></div>

  <div class="abs label" style="left:421px;top:517px">Select Enquiry Category:</div>
  <div class="abs label" style="left:521px;top:551px">Investor Enquiry</div>
  <div class="abs check" style="left:629px;top:550px"></div>
  <div class="abs label" style="left:661px;top:551px">Career Enquiry</div>
  <div class="abs check" style="left:762px;top:550px"></div>
  <div class="abs label" style="left:794px;top:551px">Other Enquiry</div>
  <div class="abs check" style="left:886px;top:550px"></div>

  <div class="abs label" style="left:421px;top:580px">Futher Description (Tell Us More...)</div>
  <div class="abs message"></div>
  <div class="abs btn btn-submit">Submit</div>

  <aside class="abs right-panel">
    <div class="panel-band" role="img" aria-label="Decorative blue wave band along the panel foot"></div>
  </aside>
  <div class="abs btn nav-btn" style="top:255px">OUR FOCUS</div>
  <div class="abs btn nav-btn" style="top:277px">CONTACT US</div>
  <div class="abs quick-title">quick links</div>
  <div class="abs quick-rule"></div>
  <div class="abs btn nav-btn soft" style="top:357px">LUDO HOME</div>
  <div class="abs btn nav-btn soft" style="top:381px">CONTACT US</div>

  <footer class="abs footer">Copyright © 2009 LUDO CAPITAL - Some rights reserved. <span class="policy">Copyright Policy</span></footer>
</div>
</body>
</html>
```